Modern business card and stationary for a dental office
World Class Care
Professional
Dr. Gavin Morrow
General Dentist
4836- 92 Street S.E. Edmonton, AB T6K 3R2
drmorrow@pinehollowdental.ca
pinehollowdental.ca
Family Clinic *Cosmetic Dentistry *Implant Dentistry *services provided by a general dentist

```html
<!DOCTYPE html>
<html lang="en">
<head>
<meta charset="utf-8">
<title>Pine Hollow Dental – Business Card</title>
<link href="https://fonts.googleapis.com/css2?family=Roboto:wght@400;700&display=swap" rel="stylesheet">
<style>
  :root {
    --page: #e6e8ec;
    --navy-deep: #0d2a57;
    --navy: #1a4a8c;
    --navy-light: #2d66ad;
    --accent: #2aa3e6;
    --white: #ffffff;
    --ink: #1d3f78;
    --muted: #d7e4f5;
  }
  * { box-sizing: border-box; margin: 0; padding: 0; }
  html, body { width: 1200px; height: 852px; overflow: hidden; }
  body {
    background: var(--page);
    font-family: "Roboto", Arial, sans-serif;
    display: flex;
    align-items: center;
    justify-content: center;
    gap: 60px;
  }
  .card {
    position: relative;
    width: 540px;
    height: 310px;
    border-radius: 18px;
    overflow: hidden;
    background: var(--white);
    box-shadow: 0 10px 30px rgba(13, 42, 87, 0.18);
  }
  .card__panel { position: absolute; inset: 0; width: 100%; height: 100%; }
  .card--back .card__panel { transform: scaleX(-1); }

  .brand {
    position: absolute;
    top: 50%;
    transform: translateY(-50%);
    display: flex;
    align-items: center;
    gap: 12px;
    color: var(--ink);
    font-weight: 700;
    font-size: 24px;
    letter-spacing: 1px;
    line-height: 1.15;
  }
  .brand__dot { width: 14px; height: 14px; border-radius: 50%; background: var(--ink); flex: none; }
  .card--front .brand { left: 318px; }
  .card--back .brand { left: 40px; }

  .details { position: absolute; top: 0; bottom: 0; color: var(--white); }
  .card--front .details { left: 24px; width: 240px; }
  .card--back .details { right: 24px; width: 240px; text-align: right; }

  .details__name { position: absolute; top: 42px; left: 0; right: 0; font-size: 17px; font-weight: 700; }
  .details__title { position: absolute; top: 64px; left: 0; right: 0; font-size: 12px; color: var(--muted); }
  .details__address { position: absolute; top: 138px; left: 0; right: 0; font-size: 12px; line-height: 1.55; color: var(--muted); }
  .contact { position: absolute; top: 200px; left: 0; right: 0; list-style: none; font-size: 12px; line-height: 19px; color: var(--muted); }
  .contact__item { display: flex; align-items: center; gap: 8px; }
  .card--back .contact__item { flex-direction: row-reverse; }
  .contact__icon { width: 12px; height: 12px; flex: none; fill: var(--white); }
</style>
</head>
<body>

<section class="card card--front">
  <svg class="card__panel" viewBox="0 0 540 310" preserveAspectRatio="none" aria-hidden="true">
    <defs>
      <linearGradient id="panelFront" x1="0" y1="0" x2="1" y2="1">
        <stop offset="0" stop-color="#2d66ad"/>
        <stop offset="0.55" stop-color="#1a4a8c"/>
        <stop offset="1" stop-color="#0d2a57"/>
      </linearGradient>
    </defs>
    <path d="M0 0 H300 Q236 155 312 310 H0 Z" fill="#2aa3e6"/>
    <path d="M0 0 H288 Q222 155 296 310 H0 Z" fill="url(#panelFront)"/>
  </svg>
  <div class="details">
    <p class="details__name">Dr. Gavin Morrow</p>
    <p class="details__title">General Dentist</p>
    <p class="details__address">4836- 92 Street S.E.<br>Edmonton, AB T6K 3R2</p>
    <ul class="contact">
      <li class="contact__item"><svg class="contact__icon" viewBox="0 0 24 24"><path d="M6.6 10.8a15 15 0 0 0 6.6 6.6l2.2-2.2a1 1 0 0 1 1-.25 11.4 11.4 0 0 0 3.6.57 1 1 0 0 1 1 1V20a1 1 0 0 1-1 1A17 17 0 0 1 3 4a1 1 0 0 1 1-1h3.5a1 1 0 0 1 1 1c0 1.25.2 2.45.57 3.57a1 1 0 0 1-.25 1z"/></svg>780-555-0142</li>
      <li class="contact__item"><svg class="contact__icon" viewBox="0 0 24 24"><path d="M7 1h10a2 2 0 0 1 2 2v18a2 2 0 0 1-2 2H7a2 2 0 0 1-2-2V3a2 2 0 0 1 2-2zm0 3v14h10V4zm5 15.2a1.2 1.2 0 1 0 0 2.4 1.2 1.2 0 0 0 0-2.4z"/></svg>780-555-0187</li>
      <li class="contact__item"><svg class="contact__icon" viewBox="0 0 24 24"><path d="M2 5h20v14H2zm2 2v.5l8 5 8-5V7l-8 5z"/></svg>drmorrow@pinehollowdental.ca</li>
      <li class="contact__item"><svg class="contact__icon" viewBox="0 0 24 24"><path d="M12 2a10 10 0 1 0 0 20 10 10 0 0 0 0-20zm6.9 6h-3a15 15 0 0 0-1.3-4 8 8 0 0 1 4.3 4zM12 4c.8 1.1 1.5 2.5 1.9 4h-3.8c.4-1.5 1.1-2.9 1.9-4zM4.3 14a8 8 0 0 1 0-4h3.4a16 16 0 0 0 0 4zm.8 2h3a15 15 0 0 0 1.3 4 8 8 0 0 1-4.3-4zm3-8h-3a8 8 0 0 1 4.3-4 15 15 0 0 0-1.3 4zM12 20c-.8-1.1-1.5-2.5-1.9-4h3.8c-.4 1.5-1.1 2.9-1.9 4zm2.3-6H9.7a14 14 0 0 1 0-4h4.6a14 14 0 0 1 0 4zm.3 6a15 15 0 0 0 1.3-4h3a8 8 0 0 1-4.3 4zm1.7-6a16 16 0 0 0 0-4h3.4a8 8 0 0 1 0 4z"/></svg>www.pinehollowdental.ca</li>
    </ul>
  </div>
  <div class="brand"><span class="brand__dot"></span><span>PINE HOLLOW<br>DENTAL</span></div>
</section>

<section class="card card--back">
  <svg class="card__panel" viewBox="0 0 540 310" preserveAspectRatio="none" aria-hidden="true">
    <defs>
      <linearGradient id="panelBack" x1="0" y1="0" x2="1" y2="1">
        <stop offset="0" stop-color="#2d66ad"/>
        <stop offset="0.55" stop-color="#1a4a8c"/>
        <stop offset="1" stop-color="#0d2a57"/>
      </linearGradient>
    </defs>
    <path d="M0 0 H290 Q226 155 302 310 H0 Z" fill="#2aa3e6"/>
    <path d="M0 0 H278 Q212 155 286 310 H0 Z" fill="url(#panelBack)"/>
  </svg>
  <div class="brand"><span class="brand__dot"></span><span>PINE HOLLOW<br>DENTAL</span></div>
  <div class="details">
    <p class="details__name">Dr. Gavin Morrow</p>
    <p class="details__title">General Dentist</p>
    <p class="details__address">4836- 92 Street S.E.<br>Edmonton, AB T6K 3R2</p>
    <ul class="contact">
      <li class="contact__item"><svg class="contact__icon" viewBox="0 0 24 24"><path d="M6.6 10.8a15 15 0 0 0 6.6 6.6l2.2-2.2a1 1 0 0 1 1-.25 11.4 11.4 0 0 0 3.6.57 1 1 0 0 1 1 1V20a1 1 0 0 1-1 1A17 17 0 0 1 3 4a1 1 0 0 1 1-1h3.5a1 1 0 0 1 1 1c0 1.25.2 2.45.57 3.57a1 1 0 0 1-.25 1z"/></svg>780-555-0142</li>
      <li class="contact__item"><svg class="contact__icon" viewBox="0 0 24 24"><path d="M7 1h10a2 2 0 0 1 2 2v18a2 2 0 0 1-2 2H7a2 2 0 0 1-2-2V3a2 2 0 0 1 2-2zm0 3v14h10V4zm5 15.2a1.2 1.2 0 1 0 0 2.4 1.2 1.2 0 0 0 0-2.4z"/></svg>780-555-0187</li>
      <li class="contact__item"><svg class="contact__icon" viewBox="0 0 24 24"><path d="M2 5h20v14H2zm2 2v.5l8 5 8-5V7l-8 5z"/></svg>drmorrow@pinehollowdental.ca</li>
      <li class="contact__item"><svg class="contact__icon" viewBox="0 0 24 24"><path d="M12 2a10 10 0 1 0 0 20 10 10 0 0 0 0-20zm6.9 6h-3a15 15 0 0 0-1.3-4 8 8 0 0 1 4.3 4zM12 4c.8 1.1 1.5 2.5 1.9 4h-3.8c.4-1.5 1.1-2.9 1.9-4zM4.3 14a8 8 0 0 1 0-4h3.4a16 16 0 0 0 0 4zm.8 2h3a15 15 0 0 0 1.3 4 8 8 0 0 1-4.3-4zm3-8h-3a8 8 0 0 1 4.3-4 15 15 0 0 0-1.3 4zM12 20c-.8-1.1-1.5-2.5-1.9-4h3.8c-.4 1.5-1.1 2.9-1.9 4zm2.3-6H9.7a14 14 0 0 1 0-4h4.6a14 14 0 0 1 0 4zm.3 6a15 15 0 0 0 1.3-4h3a8 8 0 0 1-4.3 4zm1.7-6a16 16 0 0 0 0-4h3.4a8 8 0 0 1 0 4z"/></svg>www.pinehollowdental.ca</li>
    </ul>
  </div>
</section>

</body>
</html>
```